Wordpress Design Project for Employee Communications Site

We need a Wordpress design for a company that strategizes on and produces materials for employee communications. Improving employee communications at all levels of an organization can help improve overall company performance and results. The site needs to look very clean and professional; we're not afraid of white space. We like the functionality that Wordpress provides; however, we only want one "true" blog page; the other pages should give the impression of a more "static" web site - particularly the home page. I have a logo that I can provide.

I have added these comments to the discussion page:
Great question - thank you for asking it. I’ve done more research

I like the very clean and monochromatic looks to many of these. I don’t have to have monochromatic, but I do like minimal colors. Simple, clean, organized. The home page should “fit” almost entirely without scrolling. I do like fat footers that you can scroll down to. I don’t want a colored background, but any that I’ve chosen with colored backgrounds could be switched to a white background.

http://www.minaveltrosk.com/
http://pondgrav.com/
http://v1.kelbrumwick.com/
http://howthemoss.com/
http://turnqualm.com/
http://www.interiors.pelmux.co.uk/
http://wrupgradstudio.com/

These last two are more corporate sites. The first one is from a well-respected consultant in my area who does a lot of what I do. And I think Farnquist does a nice job with their site. So, I want to marry the look I like with getting the content job done.

http://www.messagingkettle.com/
http://www.farnquist.com/view/en_US/us/index.htm

Target Market(s)

Target market is mid- to large-sized companies. More than 500 employees.

Industry/Entity Type

Communications

Requirements
Must have
• Need an impactful home page. There should be a "blog" page; contact us; services; about. For starters, at least. I want fonts to be very readable - that is, either quite dark gray or black.
Nice to have
• I am loathe to include a picture of myself, but I do want some images that say, "professional" and "expert" in communications.
Should not have
• I don't want a hits counter :) (I know no one would do that!).

```html
<!DOCTYPE html>
<html lang="en">
<head>
<meta charset="utf-8">
<title>Workforce Messaging Group – Home and Blog Pages</title>
<link href="https://fonts.googleapis.com/css2?family=Arimo:wght@400;700&display=swap" rel="stylesheet">
<style>
:root{
  --ink:#222;
  --text:#555;
  --muted:#888;
  --green:#9db52c;
  --black:#141414;
  --rule:#dedede;
  --soft:#f3f3f3;
  --footer:#eeeeee;
  --btn:#9a9a9a;
  --canvas:#ffffff;
}
*{box-sizing:border-box;margin:0;padding:0}
html,body{width:1200px;height:900px;overflow:hidden;background:var(--canvas)}
body{position:relative;font-family:"Arimo",Arial,sans-serif;color:var(--ink)}
.page{position:absolute;background:#fff;box-shadow:0 0 6px rgba(0,0,0,.22);overflow:hidden}
.page>*,.news>*,.newsletter>*,.footer>*{position:absolute}
.page-home{left:50px;top:10px;width:514px;height:870px}
.page-blog{left:620px;top:200px;width:526px;height:470px}
.topbar{left:0;top:0;width:100%;height:8px;background:var(--black)}
.tool{width:14px;height:14px;background:#333}
.tool svg{display:block}
.tool.alt{background:#999}
.brand{display:flex;align-items:center;gap:8px;font-size:19px;color:var(--ink);font-weight:400;white-space:nowrap}
.brand .dot{width:30px;height:30px;border-radius:50%;background:var(--green);flex:none}
.call{font-size:9px;font-weight:700;color:var(--ink);white-space:nowrap}
.call b{font-size:13px;font-weight:400;margin-left:4px}
.hero{left:0;top:90px;width:100%;height:230px;background:linear-gradient(100deg,#f4f6e6 0%,#d9e2a6 35%,#b8c66a 60%,#8e9a45 100%)}
.nav{display:flex;gap:4px}
.nav span{background:var(--black);color:#fff;font-size:8px;padding:6px 9px;white-space:nowrap}
.nav span.active{background:#fff;color:var(--green);border:1px solid var(--rule);border-bottom:none}
.photo{background:linear-gradient(135deg,#e6e6e6,#bdbdbd)}
h2{font-size:15px;font-weight:400;color:var(--ink);white-space:nowrap}
p.copy{font-size:7px;line-height:10px;color:var(--text)}
.more{background:var(--btn);color:#fff;font-size:7px;padding:3px 10px}
.news{border:1px solid var(--rule)}
.news .tab{left:8px;top:-1px;border:1px solid var(--rule);border-bottom:1px solid #fff;background:#fff;font-size:8px;padding:4px 8px}
.news .rule{left:0;top:16px;width:100%;height:1px;background:var(--rule)}
.news-item{left:8px;width:128px;font-size:6px;line-height:8px;color:var(--text)}
.news-item .date{font-weight:700;color:var(--ink)}
.news-item .link{color:#c66a1b;text-decoration:underline}
.news-item::after{content:"";position:absolute;left:0;bottom:-6px;width:100%;height:1px;background:var(--rule)}
ul.list{list-style:none}
ul.list li{position:relative;font-size:7px;color:var(--text);line-height:11px;border-bottom:1px solid #eee;padding-left:8px}
ul.list li::before{content:"›";position:absolute;left:0;top:0;color:var(--muted)}
.newsletter{background:var(--black);color:#fff}
.newsletter .label{left:6px;top:5px;font-size:8px;font-weight:700}
.newsletter .field{left:6px;top:26px;width:88px;height:14px;background:#fff}
.newsletter .go{left:98px;top:26px;width:38px;height:14px;background:var(--btn);font-size:6px;color:#fff;text-align:center;line-height:14px}
.footer{left:0;top:690px;width:100%;height:180px;background:var(--footer)}
.fcol h3{font-size:8px;font-weight:400;color:var(--ink);margin-bottom:6px;white-space:nowrap}
.fcol p{font-size:6px;line-height:9px;color:var(--text)}
.connect{font-size:6px;color:var(--text);white-space:nowrap;display:flex;align-items:center;gap:3px}
.connect i{width:8px;height:8px;background:#7a8fb5;display:inline-block}
.connect i+i{background:#79b7d6}
.connect i+i+i{background:#999}
.hr{height:1px;background:var(--rule)}
.datebox{width:26px;height:30px;background:var(--black);color:#fff;text-align:center;font-size:8px;line-height:10px;padding-top:4px}
.post-title{font-size:11px;color:var(--ink);white-space:nowrap}
.meta{font-size:6px;color:var(--muted);white-space:nowrap}
.fade{left:0;bottom:0;width:100%;height:150px;background:linear-gradient(to bottom,rgba(255,255,255,0),#fff 92%)}
</style>
</head>
<body>

<section class="page page-home" aria-label="Home page">
  <div class="topbar"></div>
  <div class="tool" style="left:466px;top:12px"><svg width="14" height="14"><rect x="4" y="4" width="6" height="6" fill="#fff"/></svg></div>
  <div class="tool alt" style="left:484px;top:12px"><svg width="14" height="14"><circle cx="6" cy="6" r="3" stroke="#fff" fill="none" stroke-width="1.3"/><line x1="8.2" y1="8.2" x2="11" y2="11" stroke="#fff" stroke-width="1.4"/></svg></div>

  <div class="brand" style="left:20px;top:36px"><span class="dot"></span>Workforce Messaging Group</div>
  <div class="call" style="right:20px;top:54px">Call <b>1-800-555-01-47</b></div>

  <div class="hero" role="img" aria-label="Photo of a business team meeting around a desk, in a soft green tint"></div>
  <div class="nav" style="left:18px;top:300px">
    <span class="active">About Us</span><span>Services</span><span>Blog</span><span>Contacts</span>
  </div>

  <div class="photo" style="left:16px;top:356px;width:134px;height:124px" role="img" aria-label="Group photo of smiling colleagues"></div>
  <h2 style="left:170px;top:360px">Welcome Message</h2>
  <p class="copy" style="left:170px;top:384px;width:176px">We help large organizations speak clearly to their people. Good internal messaging lifts trust, focus and daily results across every team and level.<br><br>From strategy to finished materials, we plan, write and deliver each piece with care.</p>
  <div class="more" style="left:170px;top:474px">More</div>

  <div class="news" style="left:356px;top:362px;width:144px;height:232px">
    <div class="rule"></div>
    <div class="tab">News</div>
    <div class="news-item" style="top:26px"><span class="date">07-01-2012</span> <span class="link">Quarterly Update</span><br>New survey tools help leaders hear staff.</div>
    <div class="news-item" style="top:76px"><span class="date">06-24-2012</span> <span class="link">Town Hall Guide</span><br>Tips for running open sessions with teams.</div>
    <div class="news-item" style="top:126px"><span class="date">06-11-2012</span> <span class="link">Change Toolkit</span><br>Templates that explain change in plain words.</div>
    <div class="news-item" style="top:176px"><span class="date">05-30-2012</span> <span class="link">Intranet Review</span><br>How to keep internal pages fresh and useful.</div>
  </div>

  <h2 style="left:16px;top:526px">New Services</h2>
  <ul class="list" style="left:16px;top:552px;width:136px">
    <li>Leadership Messaging</li>
    <li>Policy and Benefits Guides</li>
    <li>Internal Campaigns</li>
    <li>Program Management</li>
    <li>Employee Surveys</li>
    <li>Onboarding Materials</li>
    <li>Change Management</li>
  </ul>

  <h2 style="left:170px;top:526px">Testimonials</h2>
  <svg style="left:324px;top:530px" width="10" height="8"><rect width="10" height="8" fill="#e0e0e0"/><rect x="3" width="4" height="8" fill="#d77a2a"/></svg>
  <p class="copy" style="left:170px;top:552px;width:176px">Their team turned a complex benefits change into clear, friendly messages. Our people understood it the first time, and questions dropped sharply within a week.</p>
  <p class="copy" style="left:170px;top:616px;width:176px;color:var(--ink)">Mr Ned Holloway</p>

  <div class="newsletter" style="left:356px;top:610px;width:144px;height:48px">
    <div class="label">Newsletter Sign Up</div>
    <div class="field"></div>
    <div class="go">Subscribe</div>
  </div>

  <div class="footer">
    <div class="fcol" style="left:16px;top:16px;width:120px"><h3>About Us</h3><p>We plan and produce clear internal messages for large firms that value their people.</p></div>
    <div class="fcol" style="left:166px;top:16px;width:50px"><h3>Join In</h3><p>› Events<br>› Careers<br>› Newsletter</p></div>
    <div class="fcol" style="left:230px;top:16px;width:70px"><h3>Recent Posts</h3><p>› Writing for busy staff<br>› Clear change notes<br>› Survey results</p></div>
    <div class="fcol" style="left:324px;top:16px;width:50px"><h3>Archives</h3><p>› May, 2012<br>› April, 2012<br>› March, 2012</p></div>
    <div class="fcol" style="left:414px;top:16px;width:90px"><h3>Popular Items</h3><p>› Benefits Guide<br>› Team Briefings<br>› Intranet Plans<br>› Consulting</p></div>
    <div class="connect" style="left:420px;top:154px">Connect With Us <i></i><i></i><i></i></div>
  </div>
</section>

<section class="page page-blog" aria-label="Blog page">
  <div class="topbar" style="height:10px"></div>
  <div class="tool" style="left:478px;top:14px"><svg width="14" height="14"><rect x="4" y="4" width="6" height="6" fill="#fff"/></svg></div>
  <div class="tool alt" style="left:496px;top:14px"><svg width="14" height="14"><circle cx="6" cy="6" r="3" stroke="#fff" fill="none" stroke-width="1.3"/><line x1="8.2" y1="8.2" x2="11" y2="11" stroke="#fff" stroke-width="1.4"/></svg></div>

  <div class="brand" style="left:20px;top:24px"><span class="dot"></span>Workforce Messaging Group</div>
  <div class="call" style="right:20px;top:42px">Call <b>1-800-555-01-47</b></div>

  <div class="hr" style="left:0;top:66px;width:100%"></div>
  <div class="nav" style="left:18px;top:74px">
    <span>About Us</span><span>Services</span><span class="active">Blog</span><span>Contacts</span>
  </div>
  <div class="hr" style="left:0;top:96px;width:100%"></div>

  <h2 style="left:14px;top:132px">Blog</h2>
  <div class="datebox" style="left:14px;top:158px">14<br>July</div>
  <div class="post-title" style="left:50px;top:160px">Clear words for busy teams</div>
  <div class="meta" style="left:50px;top:176px">Posted by admin</div>
  <div class="meta" style="left:316px;top:176px">0 comments</div>
  <div class="hr" style="left:14px;top:190px;width:350px"></div>
  <div class="photo" style="left:14px;top:200px;width:126px;height:88px" role="img" aria-label="Photo of a smiling business team"></div>
  <p class="copy" style="left:150px;top:200px;width:214px">Staff read fast and skim often. Short lines, plain words and one clear ask help each note land. Here we share simple habits our writers use every day to make messages easy to follow.</p>
  <div class="more" style="left:150px;top:270px">More</div>

  <div class="datebox" style="left:14px;top:326px">14<br>July</div>
  <div class="post-title" style="left:50px;top:328px">Planning a town hall</div>
  <div class="meta" style="left:50px;top:344px">Posted by admin</div>
  <div class="meta" style="left:316px;top:344px">No comments</div>
  <div class="hr" style="left:14px;top:358px;width:350px"></div>
  <div class="photo" style="left:14px;top:368px;width:126px;height:100px" role="img" aria-label="Photo of a hand on a desk"></div>
  <p class="copy" style="left:150px;top:368px;width:214px">A good session starts well before the room fills. Set a clear goal, invite real questions and follow up soon after.</p>

  <h2 style="left:390px;top:132px">Categories</h2>
  <ul class="list" style="left:390px;top:158px;width:122px">
    <li>Leadership notes</li>
    <li>Change messaging</li>
    <li>Benefits and policy</li>
    <li>Internal campaigns</li>
    <li>Surveys and feedback</li>
    <li>Town halls</li>
    <li>Intranet tips</li>
    <li>Writing guides</li>
    <li>Onboarding</li>
    <li>Case studies</li>
  </ul>
  <h2 style="left:390px;top:314px">Archives</h2>
  <ul class="list" style="left:390px;top:340px;width:122px">
    <li>July 2011</li>
    <li>May 2011</li>
    <li>April 2011</li>
    <li>March 2011</li>
    <li>February 2011</li>
    <li>January 2011</li>
  </ul>

  <div class="fade"></div>
</section>

</body>
</html>
```